WEBSITE DESIGN - www.brindolux.com

We need a professional and modern looking website for our business. The current website was only made tentatively and can be viewed (we expect a website MUCH better than this). It needs to be simple and non-cluttered yet look modern and sophisticated. It needs to be very easy to navigate as our tarket market is people over the age of 45. Our logo is attached below and this should be incorporated plus the colours/theme should match this. We don't mind purchasing images online if your design includes these and we like it.

Any other specific questions please enquire as we want to hear them.

Target Market(s)

over 45 age english speaking westerners

Industry/Entity Type

Business

Number of Pages Required

1 page

Requirements
Must have
• -our logo (attached).
• -page tabs as those described (tabs.. but not necessarily each of these pages completed as well although this would be nice).
• -social media logos
• Pages should include: homepage, services, pricing, about us, contact us. There should also be a payments page designed which would link with the other pages but there would be no tab for this.

```html
<!DOCTYPE html>
<html lang="en">
<head>
<meta charset="utf-8">
<title>Brindolux – Computer Solutions</title>
<link href="https://fonts.googleapis.com/css2?family=Arimo:wght@400;700&family=Open+Sans:wght@400;600;700&display=swap" rel="stylesheet">
<style>
:root{
  --brown:#9a5a06;
  --brown-dark:#7d4804;
  --gold:#c8860e;
  --gold-light:#e3a93a;
  --heading:#b5650a;
  --text:#666;
  --dark:#222;
  --white:#fff;
  --rule:#e2e2e2;
}
*{box-sizing:border-box;margin:0;padding:0}
html,body{width:1200px;height:2875px;overflow:hidden}
body{font-family:"Open Sans",Arial,sans-serif;color:var(--text);background:var(--white);position:relative}
.abs{position:absolute}
/* header */
.site-header{top:0;left:0;width:1200px;height:128px;background:var(--white)}
.brand{left:100px;top:40px;display:flex;align-items:center;gap:10px}
.brand-dot{width:26px;height:26px;border-radius:50%;background:var(--gold)}
.brand-name{font-family:"Arimo",Arial,sans-serif;font-size:30px;color:var(--dark)}
.main-nav{top:58px;left:0;width:1200px;height:20px}
.main-nav a{position:absolute;font-family:"Arimo",Arial,sans-serif;font-size:14px;color:var(--dark);text-decoration:none}
.main-nav a.active{color:var(--gold)}
.search-icon{left:1085px;top:58px}
/* hero */
.hero{top:128px;left:0;width:1200px;height:514px;background:radial-gradient(ellipse at 65% 40%,#6f9ab8 0%,#2f5675 35%,#0f2234 75%,#071320 100%)}
.hero-caption{left:100px;top:335px;width:466px;height:121px;background:rgba(30,30,30,.82);padding:20px 20px}
.hero-caption h1{font-family:"Arimo",Arial,sans-serif;font-weight:400;font-size:31px;color:var(--white)}
.hero-caption p{font-family:"Arimo",Arial,sans-serif;font-size:23px;color:var(--gold-light);margin-top:8px}
.hero-arrow{top:365px}
/* section titles */
.section-title{left:0;width:1200px;text-align:center;font-family:"Arimo",Arial,sans-serif;font-size:32px;font-weight:400;color:var(--heading)}
.section-sub{left:0;width:1200px;text-align:center;font-size:13px;color:#444}
/* services */
.service{width:250px;text-align:center}
.service-ring{width:112px;height:112px;margin:0 auto;border-radius:50%;background:linear-gradient(135deg,#f0c060,#a8670a 60%,#e2a33a);display:flex;align-items:center;justify-content:center}
.service-ring span{width:96px;height:96px;border-radius:50%;background:var(--white);display:flex;align-items:center;justify-content:center}
.service h3{font-size:14px;font-weight:600;color:var(--heading);margin-top:26px}
.service p{font-size:12px;line-height:23px;margin-top:6px;white-space:nowrap}
/* pricing */
.pricing-bg{top:1070px;left:0;width:1200px;height:736px;background:linear-gradient(160deg,#3a3633 0%,#1d1b1a 45%,#2c2520 70%,#120f0d 100%)}
.pricing .section-title{color:var(--gold-light)}
.pricing .section-sub{color:#eee}
.plan{top:1202px;width:303px;height:546px;background:var(--white);text-align:center;font-size:13px;color:#333}
.plan-head{height:58px;background:var(--brown);color:var(--white);font-weight:600;font-size:17px;line-height:58px}
.plan-head.hot{background:linear-gradient(#d39a2a,#8e5306)}
.plan-row{height:31px;line-height:31px;border-bottom:1px dashed var(--rule)}
.plan-term{color:var(--gold-light);font-size:13px;margin-top:8px}
.plan-note{font-size:11.5px;line-height:19px;color:#555;padding:2px 12px 6px;border-bottom:1px solid var(--rule)}
.plan-feature{height:31px;line-height:31px;border-bottom:1px solid var(--rule)}
.plan-terms{margin-top:14px;font-size:13px;color:var(--heading);display:flex;justify-content:center;align-items:center;gap:8px}
.plan-terms i{width:12px;height:12px;border:1px solid #999;display:inline-block}
.btn{display:inline-block;background:linear-gradient(#c4831c,#8a4f05);color:var(--white);font-weight:600;font-size:13px;text-decoration:none;text-align:center}
.plan .btn{margin-top:14px;width:118px;height:40px;line-height:40px}
/* about */
.about-title{left:100px;top:1916px;font-family:"Arimo",Arial,sans-serif;font-size:34px;color:var(--heading);font-weight:400}
.about-lead{left:100px;top:1978px;width:470px;font-size:12px;line-height:23px}
.about-col{top:2048px;width:210px;font-size:12px;line-height:23px}
.about-col h4{font-size:12px;font-weight:400;color:var(--dark);text-transform:uppercase}
.about .btn{left:100px;top:2205px;width:118px;height:40px;line-height:40px}
.about-screen{left:662px;top:1858px;width:438px;height:378px;border-radius:14px 14px 0 0;background:linear-gradient(135deg,#b9c7d6 0%,#1e3f66 35%,#2c5f8e 65%,#16304f 100%)}
.about-base{left:393px;top:2236px;width:709px;height:36px;border-radius:0 0 30px 30px;background:linear-gradient(#f2f3f5,#c9ccd1)}
/* contact */
.contact-bg{top:2320px;left:0;width:1200px;height:494px;background:linear-gradient(135deg,#4d5d70 0%,#36465a 50%,#2c3a4d 100%)}
.contact .section-title{top:2352px;color:var(--gold-light)}
.contact .section-sub{top:2398px;color:var(--white);font-size:12px}
.address-box{left:157px;top:2427px;width:399px;height:353px;border:1px solid rgba(255,255,255,.8);padding:22px 20px;font-size:12px;line-height:38px;color:var(--white)}
.address-box .line{display:flex;gap:14px}
.address-box .label{color:var(--gold-light)}
.address-box .icon{width:18px;flex:none;color:var(--gold-light)}
.field{width:192px;height:38px;border:1px solid rgba(255,255,255,.85);color:var(--white);font-size:12px;line-height:36px;padding-left:8px}
.contact .btn{left:744px;top:2707px;width:115px;height:34px;line-height:34px}
/* footer */
.site-footer{top:2814px;left:0;width:1200px;height:61px;background:var(--brown);color:var(--white);font-size:11px}
.site-footer .copy{left:100px;top:24px}
.follow{left:890px;top:19px;display:flex;gap:14px;align-items:center;font-size:14px}
.follow span.dot{width:16px;height:16px;border-radius:50%;background:var(--white);display:inline-block}
</style>
</head>
<body>

<header class="site-header abs">
  <div class="brand abs"><span class="brand-dot"></span><span class="brand-name">Brindolux</span></div>
  <nav class="main-nav abs">
    <a class="active" style="left:563px">HOME</a>
    <a style="left:643px">SERVICES</a>
    <a style="left:750px">PRICING</a>
    <a style="left:845px">ABOUT US</a>
    <a style="left:952px">CONTACT US</a>
  </nav>
  <svg class="search-icon abs" width="16" height="16" viewBox="0 0 16 16"><circle cx="6.5" cy="6.5" r="4.8" fill="none" stroke="#c8860e" stroke-width="2"/><line x1="10" y1="10" x2="14.5" y2="14.5" stroke="#c8860e" stroke-width="2.4"/></svg>
</header>

<section class="hero abs" role="img" aria-label="Photo of hands typing on a laptop keyboard in cool blue light">
</section>
<svg class="hero-arrow abs" style="left:40px" width="14" height="40" viewBox="0 0 14 40"><polyline points="12,2 2,20 12,38" fill="none" stroke="rgba(255,255,255,.5)" stroke-width="2"/></svg>
<svg class="hero-arrow abs" style="left:1146px" width="14" height="40" viewBox="0 0 14 40"><polyline points="2,2 12,20 2,38" fill="none" stroke="rgba(255,255,255,.5)" stroke-width="2"/></svg>
<div class="hero-caption abs">
  <h1>Instant Support</h1>
  <p>Instant Technical Help for Your Devices</p>
</div>

<section class="services">
  <h2 class="section-title abs" style="top:695px">BEST SERVICES</h2>
  <p class="section-sub abs" style="top:756px">That's What We Do</p>

  <div class="service abs" style="left:92px;top:810px">
    <div class="service-ring"><span>
      <svg width="40" height="40" viewBox="0 0 40 40"><circle cx="20" cy="15" r="8" fill="#222"/><path d="M6 38c0-9 6-14 14-14s14 5 14 14z" fill="#222"/><path d="M9 16a11 11 0 0 1 22 0" fill="none" stroke="#222" stroke-width="2.5"/></svg>
    </span></div>
    <h3>Tech Support</h3>
    <p>We make technology easier for you<br>with instant support.</p>
  </div>
  <div class="service abs" style="left:350px;top:810px">
    <div class="service-ring"><span>
      <svg width="40" height="40" viewBox="0 0 40 40"><path d="M4 24h10l3 5h6l3-5h10v12H4z" fill="#222"/><path d="M20 4v16M13 13l7 7 7-7" fill="none" stroke="#222" stroke-width="3"/></svg>
    </span></div>
    <h3>Downloads</h3>
    <p>The best apps to optimize &amp; secure your<br>digital devices.</p>
  </div>
  <div class="service abs" style="left:605px;top:810px">
    <div class="service-ring"><span>
      <svg width="42" height="40" viewBox="0 0 42 40"><rect x="4" y="6" width="34" height="22" fill="none" stroke="#222" stroke-width="3"/><path d="M15 34h12M21 28v6" stroke="#222" stroke-width="3"/><path d="M14 22l14-12" stroke="#222" stroke-width="2.5"/></svg>
    </span></div>
    <h3>Web Design</h3>
    <p>We understand that every business<br>owner has his own way of showcasing<br>products</p>
  </div>
  <div class="service abs" style="left:862px;top:810px">
    <div class="service-ring"><span>
      <svg width="30" height="42" viewBox="0 0 30 42"><rect x="4" y="2" width="22" height="38" rx="3" fill="none" stroke="#222" stroke-width="2.5"/><circle cx="15" cy="34" r="2" fill="#222"/></svg>
    </span></div>
    <h3>Understand the Urgency</h3>
    <p>We believe in careful planning for you.</p>
  </div>
</section>

<div class="pricing-bg abs" role="img" aria-label="Dark photo of a person working at a laptop"></div>
<section class="pricing">
  <h2 class="section-title abs" style="top:1098px">BEST PRICES</h2>
  <p class="section-sub abs" style="top:1151px">Our Affordable Prices</p>

  <div class="plan abs" style="left:107px">
    <div class="plan-head">QUICK FIX</div>
    <div class="plan-row">NZD 95</div><div class="plan-row">USD 60*</div><div class="plan-row">GBP 40*</div>
    <div class="plan-term">1 MONTH</div>
    <p class="plan-note">*The price advertised might not be the same price charged to the credit card account due to exchange rate fluctuations.This means that because we are based in New Zealand we have to convert your purchase to New Zealand dollars at the exchange rate on the day it is processed.</p>
    <div class="plan-feature">1 MONTH TECH SUPPORT</div>
    <div class="plan-feature">FOR 1 COMPUTER</div>
    <div class="plan-feature">24X7 AVAILABILITY</div>
    <div class="plan-terms"><i></i>I agree to the Terms and Conditions</div>
    <a class="btn">ORDER NOW</a>
  </div>
  <div class="plan abs" style="left:449px">
    <div class="plan-head hot">STARTER</div>
    <div class="plan-row">NZD 140</div><div class="plan-row">USD 90*</div><div class="plan-row">GBP 60*</div>
    <div class="plan-term">6 MONTH</div>
    <p class="plan-note">*The price advertised might not be the same price charged to the credit card account due to exchange rate fluctuations.This means that because we are based in New Zealand we have to convert your purchase to New Zealand dollars at the exchange rate on the day it is processed.</p>
    <div class="plan-feature">6 MONTH TECH SUPPORT</div>
    <div class="plan-feature">6 MONTH SUPPORT FOR THE SAME ISSUE</div>
    <div class="plan-feature">24X7 AVAILABILITY</div>
    <div class="plan-terms"><i></i>I agree to the Terms and Conditions</div>
    <a class="btn">ORDER NOW</a>
  </div>
  <div class="plan abs" style="left:790px">
    <div class="plan-head">ADVANCE</div>
    <div class="plan-row">NZD 250</div><div class="plan-row">USD 160*</div><div class="plan-row">GBP 105*</div>
    <div class="plan-term">1 YEAR</div>
    <p class="plan-note">*The price advertised might not be the same price charged to the credit card account due to exchange rate fluctuations.This means that because we are based in New Zealand we have to convert your purchase to New Zealand dollars at the exchange rate on the day it is processed.</p>
    <div class="plan-feature">1 YEAR TECH SUPPORT</div>
    <div class="plan-feature">UPTO 3 COMPUTERS &amp; PRINTERS</div>
    <div class="plan-feature">CONNECTED DEVICES WITH ROUTER</div>
    <div class="plan-terms"><i></i>I agree to the Terms and Conditions</div>
    <a class="btn">ORDER NOW</a>
  </div>
</section>

<section class="about">
  <h2 class="about-title abs">ABOUT US</h2>
  <p class="about-lead abs">The one stop comprehensive diagnostic &amp; repair station for your computer and connected devices. We'll fix anything!</p>
  <div class="about-col abs" style="left:100px">
    <h4>Diagnosis &amp; Repair</h4>
    <p>The one stop comprehensive diagnostic &amp; repair station for your computer and connected devices. We'll fix anything!</p>
  </div>
  <div class="about-col abs" style="left:330px">
    <h4>Setup &amp; Install</h4>
    <p>Confused and frustrated with device setup &amp; installation? Leave it to the experts, which means all you've to do is sit back &amp; relax.</p>
  </div>
  <a class="btn abs">VIEW MORE</a>
  <div class="about-screen abs" role="img" aria-label="Laptop screen showing a businessman holding a phone amid network connection graphics"></div>
  <div class="about-base abs"></div>
</section>

<div class="contact-bg abs" role="img" aria-label="Street map of central Auckland"></div>
<section class="contact">
  <h2 class="section-title abs">CONTACT US</h2>
  <p class="section-sub abs">We are happy to talk with you.</p>
  <address class="address-box abs" style="font-style:normal">
    <div class="line" style="line-height:26px"><span class="icon">
      <svg width="12" height="16" viewBox="0 0 12 16"><path d="M6 0a6 6 0 0 1 6 6c0 4-6 10-6 10S0 10 0 6a6 6 0 0 1 6-6z" fill="#e3a93a"/><circle cx="6" cy="6" r="2" fill="#3b4a5e"/></svg>
    </span><span>Kestrel Computing Limited Harbourview Court Tower 1 SH/118 Marlow Street, Auckland Central, Auckland- 1010, New Zealand.</span></div>
    <div class="line" style="margin-top:8px"><span class="icon">
      <svg width="14" height="14" viewBox="0 0 14 14"><path d="M3 0l3 3-2 2c1 2 3 4 5 5l2-2 3 3-2 3C6 14 0 8 0 3z" fill="#e3a93a"/></svg>
    </span><span><span class="label">USA :</span> +1 555 014 2287</span></div>
    <div class="line"><span class="icon"></span><span><span class="label">UK :</span> +44 203 555 0147</span></div>
    <div class="line"><span class="icon"></span><span><span class="label">AUSTRALIA :</span> +61 2 5550 1932</span></div>
    <div class="line"><span class="icon">
      <svg width="16" height="12" viewBox="0 0 16 12"><rect width="16" height="12" fill="#e3a93a"/><polyline points="0,0 8,7 16,0" fill="none" stroke="#3b4a5e" stroke-width="1.5"/></svg>
    </span><span><span class="label">For Enquiry :</span> info@brindolux.com</span></div>
    <div class="line"><span class="icon"></span><span><span class="label">For Billing :</span> bills@brindolux.com</span></div>
    <div class="line"><span class="icon"></span><span><span class="label">For Support :</span> support@brindolux.com</span></div>
  </address>
  <div class="field abs" style="left:600px;top:2427px">First Name</div>
  <div class="field abs" style="left:832px;top:2427px">LastName</div>
  <div class="field abs" style="left:600px;top:2479px">Street Address</div>
  <div class="field abs" style="left:832px;top:2479px">Country</div>
  <div class="field abs" style="left:600px;top:2531px">State</div>
  <div class="field abs" style="left:832px;top:2531px">City</div>
  <div class="field abs" style="left:600px;top:2582px">Zip</div>
  <div class="field abs" style="left:832px;top:2582px">Phonenumber</div>
  <div class="field abs" style="left:600px;top:2634px">Mobile</div>
  <div class="field abs" style="left:832px;top:2634px">Email</div>
  <a class="btn abs">REGISTER</a>
</section>

<footer class="site-footer abs">
  <p class="copy abs">© 2016 Brindolux &nbsp;All right reserved &nbsp;Term of Use</p>
  <div class="follow abs">Follow Us On : <span class="dot"></span><span class="dot"></span><span class="dot"></span><span class="dot"></span></div>
</footer>

</body>
</html>
```